Bertrand Music Video and Film Production

THE FLYER SHOULD INCLUDE THIS TEXT:

"PROFESSIONAL FILM AND MUSIC VIDEO DIRECTzOR WITH OVER 10 YEARS EXPERIENCE. CLIENT LIST INCLUDES, 714, MARWICK, PALE HARBOURS, BRAMBLEGATE, THE LANTERNS, BLUE OAK, TAMSIN-JO, NELL MARIS, QRV, WILLOWTREE.
HD, SUPER 8, LIVE DVD, PROMO REELS AND VIDEOS ON TIME AND ON BUDGET."

I need to create a flyer/ad that I will use to promote myself and the services I provide.

My name is Bertrand Vellacott and I am a music video clip director and editor that can achieve great results regardless of budgets.

Working with HD and Super 8 vintage film formats to achieve the look you want.

I am a Melbourne based film maker with a huge client list; 714, Marwick, Pale Harbours, Nell Maris, Tamsin-Jo, Bramblegate, The Lanterns, Dominic Plaskett, Willowtree Marketing, QRV and Carrowvale Shire Council.

Black and white classic design. Clean and neat not too busy, almost minimal in a way. Incorpirate my initials to create a logo perhaps.

It needs to appeal and relate to various music genres including; rock, pop, soul, funk, country and folk as I make music videos for artists of many genres.

Feature my website:

www.clipvaultia.com/bertvella

Include my email address

bertrandvellacott@mailzephra.com

Many thanks

Bertrand

Target Market(s)

Music artists and bands performing all sorts of music styles from; rock, soul, funk, pop, country and folk.

Appealing also to band managers, artist representation and record labels/music publishers.

Industry/Entity Type

Artists

Requirements
Must have
• My website and email address and my name. I am a sole trader so i don't have a business name as such, just my name, Bertrand Vellacott.
Should not have
• a picture of me

```html
<!DOCTYPE html>
<html lang="en">
<head>
<meta charset="utf-8">
<title>Bertrand Vellacott – Film and Music Video Production</title>
<link href="https://fonts.googleapis.com/css2?family=Oswald:wght@300;400;600&display=swap" rel="stylesheet">
<style>
  :root {
    --ink: #111111;
    --paper: #ffffff;
    --yellow: #f6c94a;
    --night: #0b0b0b;
    --red: #c8171d;
    --grey-light: #e4e4e4;
  }
  html, body { margin: 0; padding: 0; overflow: hidden; background: var(--paper); }
  .flyer {
    position: relative;
    width: 847px;
    height: 1200px;
    overflow: hidden;
    background: var(--paper);
    font-family: "Oswald", "Arial Narrow", sans-serif;
  }
  .header {
    position: absolute; left: 0; top: 0; width: 847px; height: 424px;
  }
  .header-art {
    position: absolute; inset: 0;
    background: radial-gradient(ellipse at 50% 45%, var(--paper) 30%, var(--grey-light) 75%, #cfcfcf 100%);
  }
  .title {
    position: absolute; left: 0; right: 0; top: 112px;
    margin: 0; text-align: center;
    color: var(--ink); font-weight: 600;
    font-size: 94px; line-height: 102px; letter-spacing: 1px;
    text-transform: uppercase;
  }
  .services {
    position: absolute; left: 0; top: 424px; width: 847px; height: 333px;
    background: var(--yellow);
    box-sizing: border-box; padding: 62px 44px 0;
  }
  .services p {
    margin: 0; text-align: center; color: var(--ink);
    font-weight: 400; font-size: 29px; line-height: 41px;
    text-transform: uppercase; letter-spacing: 0.3px;
  }
  .contact-band {
    position: absolute; left: 0; top: 757px; width: 847px; height: 443px;
    background: var(--night);
  }
  .contact-art {
    position: absolute; right: 0; top: 0; width: 560px; height: 443px;
    background: radial-gradient(circle at 62% 55%, #5a5a5a 0%, #2a2a2a 40%, var(--night) 72%);
  }
  .name {
    position: absolute; left: 30px; top: 92px; margin: 0;
    color: var(--paper); font-weight: 300;
    font-size: 64px; line-height: 76px; letter-spacing: 2px;
    text-transform: uppercase;
  }
  .web {
    position: absolute; left: 0; top: 279px; width: 430px; height: 34px;
    background: var(--red); color: var(--paper);
    font-size: 22px; line-height: 34px; padding-left: 28px; box-sizing: border-box;
  }
  .email {
    position: absolute; left: 0; top: 321px; width: 430px; height: 32px;
    background: var(--paper); color: var(--red);
    font-size: 20px; line-height: 32px; padding-left: 10px; box-sizing: border-box;
  }
</style>
</head>
<body>
<main class="flyer">
  <header class="header">
    <div class="header-art" role="img" aria-label="Grunge collage of musical notes, speakers, vinyl records and ink splatters in grey tones"></div>
    <h1 class="title">Film and Music<br>Video Production</h1>
  </header>

  <section class="services">
    <p>Professional film and music video director with over 10 years experience. Client list includes, 714, Marwick, Pale Harbours, Bramblegate, The Lanterns, Blue Oak, Tamsin-Jo, Nell Maris, QRV, Willowtree. HD, Super 8, live DVD, promo reels and videos on time and on budget.</p>
  </section>

  <footer class="contact-band">
    <div class="contact-art" role="img" aria-label="Silhouette illustration of a DJ at turntables surrounded by swirling graphic shapes in black and grey"></div>
    <h2 class="name">Bertrand<br>Vellacott</h2>
    <div class="web">web: www.clipvaultia.com/bertvella</div>
    <div class="email">email:bertrandvellacott@mailzephra.com</div>
  </footer>
</main>
</body>
</html>
```